Q-Rolls Business Card

We are a modern retail clothing store. Established in 1994. I need a presentable card that will amaze vendors when given to them.

Front: Logo in middle
Info Side:

Name: Tomas Velder
Cell: 630-812-4463
Work: 630-917-3384 EXT. 417
Email: Tomas@q-rolls-example.com
Website: www.Q-rolls-example.com

Industry/Entity Type

Business

```html
<!DOCTYPE html>
<html lang="en">
<head>
<meta charset="utf-8">
<title>Q-Rolls Business Card</title>
<link href="https://fonts.googleapis.com/css2?family=Lato:wght@400;700;900&display=swap" rel="stylesheet">
<style>
  :root {
    --page-bg: #1c1c1c;
    --card-dark: #2a2a2a;
    --card-light: #f4f4f4;
    --ink: #1e1e1e;
    --ink-soft: #555555;
    --rule: #6a6a6a;
    --band: #8a8a8a;
    --map-dark: #353535;
    --map-light: #e2e2e2;
    --white: #ffffff;
  }
  * { box-sizing: border-box; margin: 0; padding: 0; }
  html, body { width: 1200px; height: 873px; overflow: hidden; }
  body {
    background: var(--page-bg);
    font-family: "Lato", sans-serif;
    display: flex;
    align-items: center;
    justify-content: center;
    gap: 40px;
  }
  .card {
    position: relative;
    width: 540px;
    height: 309px;
    overflow: hidden;
  }

  /* Front side */
  .card-front { background: var(--card-dark); }
  .card-front .world-map {
    position: absolute;
    left: 90px; top: 50px;
    width: 360px; height: 190px;
    background: radial-gradient(ellipse at center, var(--map-dark), var(--card-dark) 75%);
  }
  .card-front .brand {
    position: absolute;
    left: 0; right: 0; top: 100px;
    text-align: center;
    color: var(--white);
    font-weight: 900;
    font-size: 70px;
    letter-spacing: 4px;
    text-transform: uppercase;
  }
  .card-front .website {
    position: absolute;
    left: 0; right: 0; top: 212px;
    text-align: center;
    color: #cfcfcf;
    font-weight: 700;
    font-size: 15px;
  }

  /* Info side */
  .card-info { background: var(--card-light); }
  .card-info .world-map {
    position: absolute;
    left: 60px; top: 40px;
    width: 400px; height: 200px;
    background: radial-gradient(ellipse at center, var(--map-light), var(--card-light) 75%);
  }
  .card-info .brand {
    position: absolute;
    left: 210px; top: 30px;
    color: var(--ink);
    font-weight: 900;
    font-size: 38px;
    letter-spacing: 2px;
    text-transform: uppercase;
  }
  .card-info .tagline {
    position: absolute;
    left: 246px; top: 76px;
    color: var(--ink);
    font-weight: 400;
    font-size: 11px;
    letter-spacing: 1px;
  }
  .person {
    position: absolute;
    right: 40px; top: 100px;
    text-align: left;
  }
  .person .name { font-weight: 700; font-size: 16px; color: var(--ink); }
  .person .role { font-size: 12px; color: var(--ink-soft); margin-top: 3px; }
  .divider {
    position: absolute;
    left: 40px; top: 160px;
    width: 300px; height: 2px;
    background: var(--rule);
  }
  .address {
    position: absolute;
    right: 40px; top: 180px;
    text-align: right;
    font-weight: 700;
    font-size: 12.5px;
    line-height: 1.55;
    color: var(--ink);
  }
  .contacts {
    position: absolute;
    left: 40px; top: 186px;
    list-style: none;
  }
  .contacts li {
    display: flex;
    align-items: center;
    gap: 12px;
    font-size: 13.5px;
    color: var(--ink-soft);
    height: 26px;
  }
  .contacts svg { width: 14px; height: 14px; fill: var(--ink); flex: none; }
  .bottom-band {
    position: absolute;
    left: 0; bottom: 0;
    width: 540px; height: 20px;
  }
</style>
</head>
<body>
  <section class="card card-front" aria-label="Card front">
    <div class="world-map" role="img" aria-label="Faint dotted world map"></div>
    <div class="brand">Q-Rolls</div>
    <div class="website">www.Q-rolls-example.com</div>
  </section>

  <section class="card card-info" aria-label="Card info side">
    <div class="world-map" role="img" aria-label="Faint dotted world map"></div>
    <div class="brand">Q-Rolls</div>
    <div class="tagline">Fashion Retailer</div>

    <div class="person">
      <div class="name">Tomas Velder</div>
      <div class="role">Owner / Founder</div>
    </div>

    <div class="divider"></div>

    <div class="address">118 Harrow Lane,<br>Westfield IL 60999, United States</div>

    <ul class="contacts">
      <li>
        <svg viewBox="0 0 16 16" aria-hidden="true"><path d="M2 6c0-2 2-3 6-3s6 1 6 3v1h-3V5.5H5V7H2z M3 8h10l1 5H2z"/></svg>
        630-917-3384 EXT. 417
      </li>
      <li>
        <svg viewBox="0 0 16 16" aria-hidden="true"><path d="M4 1h8v14H4z M5.3 2.5v9.5h5.4V2.5z" fill-rule="evenodd"/></svg>
        630-812-4463
      </li>
      <li>
        <svg viewBox="0 0 16 16" aria-hidden="true"><path d="M1 3h14v10H1z M2.2 4.2 8 8.6l5.8-4.4z" fill-rule="evenodd"/></svg>
        tomas@q-rolls-example.com
      </li>
    </ul>

    <svg class="bottom-band" viewBox="0 0 540 20" aria-hidden="true">
      <path d="M0 8H450Q462 8 466 0H540V20H0z" fill="var(--band)"/>
      <path d="M0 6H448Q460 6 464 0" fill="none" stroke="var(--rule)" stroke-width="1.5"/>
    </svg>
  </section>
</body>
</html>
```